New Website for novelty yarn producer

We need a new website for our company, Tarvek. We make highly tailored yarns for weavers worldwide. This year marks our 40th anniversary and we want to evolve our image and identity.

Our temporary website can be found at:
www.tarvekyarns.com

Our only concern in that throughout the website the protagonist must be our client, we make their creations possible and are highly adaptable both during the ideation process of the yarn as well as in the production. This is at the core of the way we do business and is summarised within the concept of FPM (Fluid Partner Method).

Industry/Entity Type

Textile

Number of Pages Required

1 page

Colors
9bcb3c

Requirements
Must have
• Fluid Partner Method (FPM) - can be found on or current website www.tarvekyarns.com

```html
<!DOCTYPE html>
<html lang="en">
<head>
<meta charset="utf-8">
<title>Tarvek – Tailored solution for you</title>
<link href="https://fonts.googleapis.com/css2?family=Lato:wght@300;400;700&display=swap" rel="stylesheet">
<style>
:root{
  --green:#9bcb3c;
  --green-light:#b8e35c;
  --sky:#8fd6ee;
  --ink:#333;
  --mute:#555;
  --paper:#f4faea;
  --footer:#3e3e3e;
  --line:#9bbf6a;
}
*{box-sizing:border-box;margin:0;padding:0}
html,body{width:1200px;height:2936px;overflow:hidden}
body{font-family:'Lato',sans-serif;color:var(--ink);background:var(--paper);position:relative}
.abs{position:absolute}
/* hero */
.hero{position:absolute;left:0;top:0;width:1200px;height:835px;overflow:hidden;
  background:linear-gradient(180deg,#4e4e4e 0%,#5c5c5c 35%,#7a7a7a 65%,#a8a8a8 88%,#cfcfcf 100%)}
.hero-photo{position:absolute;inset:0;background:radial-gradient(ellipse at 75% 55%,rgba(20,20,20,.35),rgba(0,0,0,0) 55%),linear-gradient(100deg,rgba(255,255,255,.18),rgba(0,0,0,0) 40%)}
.menu-icon{left:113px;top:28px;width:24px}
.menu-icon span{display:block;height:2px;background:var(--green);margin-bottom:5px}
.nav{left:112px;top:68px;list-style:none}
.nav li{display:flex;align-items:center;height:39px;font-size:13px;color:#fff}
.nav li.active{color:var(--green)}
.nav svg{width:22px;height:22px;margin-right:14px}
.btn{display:inline-flex;align-items:center;justify-content:center;border:1px solid var(--green);font-size:9px;text-transform:uppercase;color:#222;background:rgba(155,203,60,.55);outline:1px solid rgba(255,255,255,.6);outline-offset:2px}
.btn.ghost{background:rgba(155,203,60,.25);color:#fff}
.contact-btn{left:1004px;top:32px;width:80px;height:24px;color:#222}
.headline{left:0;width:1200px;top:140px;text-align:center;font-weight:400;font-size:40px;letter-spacing:1px;
  background:linear-gradient(90deg,var(--sky),var(--green-light));-webkit-background-clip:text;background-clip:text;color:transparent}
.subline{left:0;width:1200px;top:192px;text-align:center;font-weight:700;font-size:16px;color:#fff}
.hero-btn{top:242px;width:84px;height:24px}
.seal{left:555px;top:370px;width:90px;height:90px;border-radius:50%;background:var(--green)}
.intro{left:372px;top:428px;width:450px;height:152px;border:1px solid var(--line);border-top:none;padding:38px 14px 0;text-align:center;font-size:12px;line-height:1.45;color:#fff;background:rgba(40,40,40,.3)}
.intro .brand{display:block;font-size:14px;font-weight:700;color:#fff;margin-bottom:4px}
.step{width:136px;height:118px;background:var(--green);border:1px solid #fff;text-align:center;color:#2b3a12}
.step h3{font-weight:300;font-size:13px;letter-spacing:1px;color:#3a5a10;background:rgba(255,255,255,.35);padding:2px 0;margin-bottom:4px;white-space:nowrap}
.step p{font-size:9px;line-height:1.35;padding:0 6px}
.learn{width:80px;height:20px;font-size:8px}
/* sections */
.section-title{left:0;width:1200px;text-align:center;font-weight:400;color:#222}
.hline{height:1px;background:var(--line)}
.body-text{left:180px;width:840px;text-align:center;font-size:14px;line-height:1.55;color:var(--mute);font-weight:300}
.num-circle{width:64px;height:46px}
.num-label{width:240px;text-align:center;font-size:14px}
.tagline{left:0;width:1200px;text-align:center;font-size:17px;font-weight:300;line-height:1.7;
  background:linear-gradient(90deg,#5fb6d6,#8fbf2c);-webkit-background-clip:text;background-clip:text;color:transparent}
.offer-label{width:240px;text-align:center;font-size:13px}
.offer-text{width:180px;text-align:center;font-size:11px;line-height:1.45;color:#222}
/* products */
.tile{position:absolute;overflow:hidden}
.tile .cap{position:absolute;left:0;top:0;padding:4px 8px 6px;color:#fff;background:rgba(120,120,120,.55)}
.tile .cap b{display:block;font-size:13px;font-weight:700}
.tile .cap i{display:block;font-style:normal;font-size:10px;opacity:.85}
/* footer */
.footer{left:0;top:2662px;width:1200px;height:274px;background:var(--footer);border-top:3px solid var(--green);color:#fff}
.footer h4{font-size:13px;font-weight:700}
.field{background:var(--green);border:1px solid #d7ebb0;font-size:10px;color:#fff;padding:3px 6px}
.flabel{font-size:11px}
.clients{list-style:none;font-size:10px;line-height:26px}
.clients li::before{content:"• ";color:var(--green)}
.contact-row{display:flex;align-items:center;font-size:10px;height:32px}
.contact-row svg{width:20px;height:20px;margin-right:12px}
</style>
</head>
<body>

<header class="hero">
  <div class="hero-photo" role="img" aria-label="Black and white photograph of knitting needles in a ball of dark yarn with a chunky woven knit"></div>
  <div class="abs menu-icon"><span></span><span></span><span></span></div>
  <ul class="abs nav">
    <li class="active"><svg viewBox="0 0 24 24" fill="none" stroke="#9bcb3c" stroke-width="1.5"><path d="M3 11 12 4l9 7v9H3z"/></svg>Home</li>
    <li><svg viewBox="0 0 24 24" fill="none" stroke="#fff" stroke-width="1.5"><circle cx="12" cy="7" r="4"/><path d="M4 21c0-5 16-5 16 0"/></svg>About Us</li>
    <li><svg viewBox="0 0 24 24" fill="none" stroke="#fff" stroke-width="1.5"><circle cx="12" cy="12" r="8"/><circle cx="12" cy="12" r="3"/></svg>Fluid Partner Method</li>
    <li><svg viewBox="0 0 24 24" fill="none" stroke="#fff" stroke-width="1.5"><rect x="4" y="4" width="16" height="16"/><path d="M4 10h16M10 4v16"/></svg>Herritage</li>
    <li><svg viewBox="0 0 24 24" fill="none" stroke="#fff" stroke-width="1.5"><rect x="4" y="3" width="16" height="18"/><path d="M8 8h8M8 12h8M8 16h5"/></svg>Blog</li>
    <li><svg viewBox="0 0 24 24" fill="none" stroke="#fff" stroke-width="1.5"><ellipse cx="12" cy="6" rx="6" ry="3"/><path d="M6 6v12c0 2 12 2 12 0V6"/></svg>Product</li>
    <li><svg viewBox="0 0 24 24" fill="none" stroke="#fff" stroke-width="1.5"><path d="M3 12 12 3h9v9l-9 9z"/><circle cx="16" cy="8" r="1.5"/></svg>Offers</li>
  </ul>
  <div class="abs btn contact-btn">Contact us</div>
  <h1 class="abs headline">TAILORED SOLUTION FOR YOU</h1>
  <p class="abs subline">Our focus is our client,The success of a client is our success.</p>
  <div class="abs btn ghost hero-btn" style="left:512px">Shop now</div>
  <div class="abs btn ghost hero-btn" style="left:605px">Services</div>

  <div class="abs hline" style="left:212px;top:425px;width:343px"></div>
  <div class="abs hline" style="left:645px;top:425px;width:330px"></div>
  <div class="abs" style="left:212px;top:425px;width:1px;height:225px;background:var(--line)"></div>
  <div class="abs" style="left:974px;top:425px;width:1px;height:225px;background:var(--line)"></div>
  <div class="abs" style="left:600px;top:580px;width:1px;height:70px;background:var(--line)"></div>

  <div class="abs intro"><span class="brand">Tarvek</span>We believe that the key to delivering a yarn that exceeds our client's expectation is to work together with weavers from step one, starting from the desired end product and working backwards. This allows us to develop the product that our weavers need.</div>
  <div class="abs seal"></div>

  <div class="abs step" style="left:143px;top:650px"><h3>IDEATION</h3><p>We define goal and parameters meeting with all the players, designers, technicians, sales force and logistics. We analyse together all aspects and...</p></div>
  <div class="abs step" style="left:531px;top:650px"><h3>EXECUTION</h3><p>Once the goals are defined our FPM team starts staging internal meetings and working with technicians, technical partners and raw material suppliers...</p></div>
  <div class="abs step" style="left:893px;top:650px;width:162px"><h3>SCALING PRODUCTION</h3><p>When the novelty yarn is defined, the process of scaling up starts, putting the value added product into production at an industrial scale making sure through...</p></div>
  <div class="abs btn ghost learn" style="left:172px;top:785px">Learn more</div>
  <div class="abs btn ghost learn" style="left:561px;top:785px">Learn more</div>
  <div class="abs btn ghost learn" style="left:935px;top:785px">Learn more</div>
</header>

<main>
  <div class="abs hline" style="left:0;top:893px;width:470px"></div>
  <div class="abs hline" style="left:730px;top:893px;width:470px"></div>
  <h2 class="abs section-title" style="top:875px;font-size:27px">Working whit US</h2>
  <p class="abs body-text" style="top:928px">Our team has decades of experience in providing yarn solutions to weavers around the world, assisting them in the creation of outstanding textiles.Our clients can expect open lines of communication, clarity and professionality<br>Our focus is our client. The success of a client is our success.</p>
  <div class="abs btn" style="left:556px;top:1022px;width:88px;height:24px">Our heritage</div>

  <h2 class="abs section-title" style="top:1088px;font-size:28px;font-weight:400"><span style="color:var(--green)">TVNS</span> IN NUMBERS</h2>
  <svg class="abs num-circle" style="left:218px;top:1147px" viewBox="0 0 64 46"><ellipse cx="32" cy="23" rx="30" ry="22" fill="#bfe3ea"/><ellipse cx="32" cy="23" rx="22" ry="20" fill="#5fc0c9"/><circle cx="32" cy="23" r="17" fill="#9bcb3c"/><text x="32" y="29" text-anchor="middle" font-family="Lato,sans-serif" font-size="17" fill="#2b3a12">40</text></svg>
  <svg class="abs num-circle" style="left:568px;top:1147px" viewBox="0 0 64 46"><ellipse cx="32" cy="23" rx="30" ry="22" fill="#bfe3ea"/><ellipse cx="32" cy="23" rx="22" ry="20" fill="#5fc0c9"/><circle cx="32" cy="23" r="17" fill="#9bcb3c"/><text x="32" y="29" text-anchor="middle" font-family="Lato,sans-serif" font-size="17" fill="#2b3a12">2</text></svg>
  <svg class="abs num-circle" style="left:885px;top:1147px" viewBox="0 0 64 46"><ellipse cx="32" cy="23" rx="30" ry="22" fill="#bfe3ea"/><ellipse cx="32" cy="23" rx="22" ry="20" fill="#5fc0c9"/><circle cx="32" cy="23" r="17" fill="#9bcb3c"/><text x="32" y="29" text-anchor="middle" font-family="Lato,sans-serif" font-size="17" fill="#2b3a12">8</text></svg>
  <div class="abs num-label" style="left:130px;top:1202px">Years in business</div>
  <div class="abs num-label" style="left:480px;top:1202px">Million Kilograms/ YR</div>
  <div class="abs num-label" style="left:797px;top:1202px">Brands</div>
  <p class="abs tagline" style="top:1254px">TVNS combines the experience of a team &nbsp;that has served the weaving industry for over 40 years,<br>fully dedicated to the success of our clients</p>

  <div class="abs hline" style="left:0;top:1362px;width:520px"></div>
  <div class="abs hline" style="left:680px;top:1362px;width:520px"></div>
  <h2 class="abs section-title" style="top:1343px;font-size:28px;font-weight:300">Our offers</h2>
  <div class="abs hline" style="left:0;top:1483px;width:1200px"></div>
  <div class="abs offer-label" style="left:100px;top:1398px">Network</div>
  <div class="abs offer-label" style="left:480px;top:1398px">Logistics</div>
  <div class="abs offer-label" style="left:855px;top:1398px">Production</div>
  <svg class="abs" style="left:124px;top:1426px" width="192" height="112" viewBox="0 0 192 112"><ellipse cx="96" cy="56" rx="94" ry="54" fill="#d4eef0" stroke="#4fb7c4"/><ellipse cx="96" cy="56" rx="78" ry="52" fill="#bfe7d0" stroke="#4fb7c4"/><ellipse cx="96" cy="56" rx="62" ry="50" fill="#5fc0b4" stroke="#fff"/><circle cx="96" cy="56" r="44" fill="#9bcb3c"/><circle cx="96" cy="56" r="13" fill="none" stroke="#111" stroke-width="3"/><path d="M90 56l4 4 8-8" fill="none" stroke="#111" stroke-width="3"/><g stroke="#111" stroke-width="3"><path d="M96 43V28M96 69v15M83 56H68M109 56h15M87 47l-9-9M105 47l9-9M87 65l-9 9M105 65l9 9"/></g><g fill="#111"><circle cx="96" cy="26" r="4"/><circle cx="96" cy="86" r="4"/><circle cx="66" cy="56" r="4"/><circle cx="126" cy="56" r="4"/><circle cx="76" cy="36" r="4"/><circle cx="116" cy="36" r="4"/><circle cx="76" cy="76" r="4"/><circle cx="116" cy="76" r="4"/></g></svg>
  <svg class="abs" style="left:504px;top:1426px" width="192" height="112" viewBox="0 0 192 112"><ellipse cx="96" cy="56" rx="94" ry="54" fill="#d4eef0" stroke="#4fb7c4"/><ellipse cx="96" cy="56" rx="78" ry="52" fill="#bfe7d0" stroke="#4fb7c4"/><ellipse cx="96" cy="56" rx="62" ry="50" fill="#5fc0b4" stroke="#fff"/><circle cx="96" cy="56" r="44" fill="#9bcb3c"/><circle cx="96" cy="56" r="30" fill="none" stroke="#111" stroke-width="2.5"/><path d="M82 78V52l14-14 14 14v26M90 78V60h12v18" fill="none" stroke="#111" stroke-width="2.5"/></svg>
  <svg class="abs" style="left:879px;top:1426px" width="192" height="112" viewBox="0 0 192 112"><ellipse cx="96" cy="56" rx="94" ry="54" fill="#d4eef0" stroke="#4fb7c4"/><ellipse cx="96" cy="56" rx="78" ry="52" fill="#bfe7d0" stroke="#4fb7c4"/><ellipse cx="96" cy="56" rx="62" ry="50" fill="#5fc0b4" stroke="#fff"/><circle cx="96" cy="56" r="44" fill="#9bcb3c"/><g fill="none" stroke="#111" stroke-width="2.5"><rect x="68" y="36" width="14" height="40"/><rect x="88" y="48" width="12" height="12"/><rect x="104" y="48" width="12" height="12"/><path d="M84 68h44"/><circle cx="92" cy="72" r="4"/><circle cx="106" cy="72" r="4"/><circle cx="120" cy="72" r="4"/></g></svg>
  <p class="abs offer-text" style="left:130px;top:1552px">A network of weavers, yarn producers and representatives consolidated over 40 years of successful business operations</p>
  <p class="abs offer-text" style="left:510px;top:1552px">With a distribution grid organized and tuned to perfection, we bring your yarns where you need them, when you need them</p>
  <p class="abs offer-text" style="left:885px;top:1552px">Production line is dynamic and solid, allowing for freedom as well as precision in any project</p>

  <div class="abs hline" style="left:0;top:1664px;width:530px"></div>
  <div class="abs hline" style="left:670px;top:1664px;width:530px"></div>
  <h2 class="abs section-title" style="top:1646px;font-size:28px;font-weight:300">Products</h2>

  <section aria-label="Products">
    <div class="tile" style="left:150px;top:1705px;width:226px;height:225px;background:linear-gradient(135deg,#2a8fb0,#45b3d0 50%,#3a4b52)" role="img" aria-label="Turquoise patterned fabric"><div class="cap"><b>Lorem</b><i>Ipsum dolor sit</i></div></div>
    <div class="tile" style="left:379px;top:1705px;width:226px;height:455px;background:linear-gradient(160deg,#5b8fd0,#3f73b8 60%,#2e5a98)" role="img" aria-label="Close-up of blue yarn threads"><div class="cap"><b>Yarn</b><i>Organic yarn</i></div></div>
    <div class="tile" style="left:608px;top:1705px;width:444px;height:225px;background:radial-gradient(circle at 40% 40%,#c8d07a,#9a8a5a 45%,#6a5a48)" role="img" aria-label="Assorted yarn cones with coloured tops"><div class="cap"><b>Cone</b><i>Multi Tinted Yarn Cones</i></div></div>
    <div class="tile" style="left:150px;top:1934px;width:226px;height:226px;background:#fff" role="img" aria-label="Orange yarn cone on white"><div class="abs" style="left:88px;top:50px;width:52px;height:150px;border-radius:8px;background:linear-gradient(90deg,#b8742c,#e3a156,#b8742c)"></div><div class="cap"><b>Cone</b><i>Super soft yarns</i></div></div>
    <div class="tile" style="left:608px;top:1934px;width:444px;height:226px;background:linear-gradient(180deg,#c8324a,#a01c2c 40%,#d6c23a 75%,#2a9fc4)" role="img" aria-label="Stack of folded carpets in red, yellow and blue"><div class="cap"><b>Carpet</b><i>Ipsum dolor sit</i></div></div>
    <div class="tile" style="left:150px;top:2163px;width:226px;height:226px;background:linear-gradient(160deg,#8a7a6a,#c0b4a4 50%,#4a4038)" role="img" aria-label="Soft feather yarn close-up"><div class="cap"><b>Yarn</b><i>Soft feather yarn</i></div></div>
    <div class="tile" style="left:379px;top:2163px;width:226px;height:454px;background:#fff" role="img" aria-label="Red yarn cone on white"><div class="abs" style="left:40px;top:60px;width:146px;height:330px;border-radius:14px;background:linear-gradient(90deg,#a8142c,#dd2a48,#a8142c)"></div><div class="cap"><b>Cone</b><i>Hot selling factory knitting 100%</i></div></div>
    <div class="tile" style="left:608px;top:2163px;width:213px;height:226px;background:linear-gradient(135deg,#2a2a2a,#8a8a8a 50%,#1e1e1e)" role="img" aria-label="Black and grey damask fabric"><div class="cap"><b>Donec</b><i>Venenatis faucibus</i></div></div>
    <div class="tile" style="left:824px;top:2163px;width:228px;height:226px;background:linear-gradient(90deg,#1a1840,#2c2a6a 50%,#151336)" role="img" aria-label="Dark blue cashmere wool"><div class="cap"><b>Wool</b><i>Winter hot cashmere</i></div></div>
    <div class="tile" style="left:150px;top:2392px;width:226px;height:225px;background:linear-gradient(180deg,#8a5a3a,#c26a3a 40%,#4a2a1a)" role="img" aria-label="Stacked rust and brown fabric"><div class="cap"><b>Loram</b><i>Quisque rutrum</i></div></div>
    <div class="tile" style="left:608px;top:2392px;width:444px;height:225px;background:linear-gradient(90deg,#d8cc8a,#9ab0c8 30%,#c87a8a 55%,#b84a5a 75%,#8aa0b8)" role="img" aria-label="Woven fabric swatches in pastel stripes"><div class="cap"><b>Lorem</b><i>Commodo nec</i></div></div>
  </section>
</main>

<footer class="abs footer">
  <h4 class="abs" style="left:150px;top:35px">Get in touch with our sales team and find out more :</h4>
  <span class="abs flabel" style="left:150px;top:78px">Name :</span>
  <div class="abs field" style="left:206px;top:74px;width:90px;height:20px">First..</div>
  <div class="abs field" style="left:302px;top:74px;width:90px;height:20px">Last...</div>
  <span class="abs flabel" style="left:150px;top:108px">Email :</span>
  <div class="abs field" style="left:206px;top:104px;width:186px;height:20px">Email...</div>
  <span class="abs flabel" style="left:150px;top:150px">Comment :</span>
  <div class="abs field" style="left:206px;top:133px;width:186px;height:60px">Ask...</div>
  <div class="abs field" style="left:254px;top:200px;width:90px;height:20px;text-align:center">Submit</div>

  <h4 class="abs" style="left:588px;top:35px">Our Client</h4>
  <ul class="abs clients" style="left:590px;top:58px">
    <li>Tarvek</li><li>Verdan</li><li>Morlo</li><li>Castel U.S.A</li><li>Fibrantis</li><li>Tarvek NYS</li><li>Romania</li>
  </ul>

  <h4 class="abs" style="left:787px;top:35px">Contact</h4>
  <div class="abs" style="left:787px;top:62px">
    <div class="contact-row"><svg viewBox="0 0 24 24" fill="#fff"><path d="M6 3l4 4-2 3c1 2 4 5 6 6l3-2 4 4-3 3C10 21 3 14 3 6z"/></svg>0574 000123</div>
    <div class="contact-row"><svg viewBox="0 0 24 24" fill="none" stroke="#fff" stroke-width="2"><path d="M12 22s7-7 7-12a7 7 0 0 0-14 0c0 5 7 12 7 12z"/><circle cx="12" cy="10" r="2.5"/></svg>Via dei Tessitori 12 - 59100 Prato - Italy</div>
    <div class="contact-row"><svg viewBox="0 0 24 24" fill="none" stroke="#fff" stroke-width="2"><circle cx="12" cy="12" r="9"/><circle cx="12" cy="12" r="3.5"/></svg>commerciale@tarvek.it</div>
    <div class="contact-row"><svg viewBox="0 0 24 24" fill="none" stroke="#fff" stroke-width="2"><rect x="3" y="8" width="18" height="12"/><path d="M7 8V3h10v5M7 13h10"/></svg>0574 000456</div>
  </div>
</footer>

</body>
</html>
```